Seeking Talented PSD Designer for Real Estate Finance Web Site

Hello ...
Need a minimalist design for a high - end finance web site that conveys prestige / sophistication / class ... Below are comps for this project ...
http://www.copperlanefunding.com/
http://mirowayfunding.com/
http://www.tolvinedgp.com/
http://quillanfunding.com/
Look forward too receiving proposals for this project ....
Target Market(s)
Commerciale entities seeking more than $500.0 k in interim capital ... These could include apartment owners / construction managers / restaurant owners / hotels / golf courses ...
Industry/Entity Type
Real Estate
Number of Pages Required
1 page
Requirements
Must have
- Super high quality graphic design ... Has to be marketable and convert customers to contact us ...
- Please refer to logo concept four ....
Should not have
- clunky / poor fonts /

```html
<!DOCTYPE html>
<html lang="en">
<head>
<meta charset="utf-8">
<title>Harrowgate Capital</title>
<link href="https://fonts.googleapis.com/css2?family=Roboto+Condensed:wght@400;700&family=Open+Sans:wght@400;600;700&display=swap" rel="stylesheet">
<style>
:root{
  --navy:#2d4068;
  --navy-dark:#263860;
  --grey-text:#8c8c8c;
  --body-text:#6a6a6a;
  --panel:#e2e3e6;
  --tab:#9b9b9b;
  --white:#ffffff;
  --rule:#4a5b80;
}
*{margin:0;padding:0;box-sizing:border-box}
html,body{width:753px;height:1200px;overflow:hidden;background:var(--white)}
body{position:relative;font-family:"Open Sans",sans-serif;color:var(--body-text)}
.abs{position:absolute}
.hero{left:0;top:0;width:753px;height:338px;
  background:linear-gradient(180deg,#b9cbe0 0%,#c8d3dd 28%,#8a8f95 60%,#5d5d5e 100%)}
.hero-glow{left:0;top:0;width:753px;height:338px;
  background:radial-gradient(circle at 730px 40px,rgba(255,244,210,.9) 0,rgba(255,244,210,0) 220px)}
.brand-mark{left:334px;top:46px;width:92px;height:92px;border-radius:50%;background:var(--navy)}
.brand-name{left:0;top:150px;width:753px;text-align:center;font-family:"Roboto Condensed",sans-serif;
  font-weight:400;font-size:34px;letter-spacing:4px;color:var(--navy);line-height:1.1}
.nav{left:0;top:338px;width:753px;height:39px;background:var(--navy)}
.nav a{position:absolute;top:0;height:39px;line-height:39px;font-family:"Roboto Condensed",sans-serif;
  font-size:14px;color:var(--white);text-decoration:none}
.nav .current{background:var(--tab);color:#1d1d1d;padding:0 24px;left:49px}
.welcome-title,.news-title{left:0;width:753px;text-align:center;font-family:"Roboto Condensed",sans-serif;
  font-size:27px;color:var(--grey-text);line-height:1}
.welcome-title{top:410px}
.welcome-title strong,.news-title strong{font-weight:400;color:var(--navy)}
.welcome-text{left:110px;top:449px;width:533px;text-align:center;font-size:10px;line-height:16px}
.card{top:525px;width:196px}
.card-photo{width:196px;height:98px}
.card h2{margin-top:12px;text-align:center;font-family:"Roboto Condensed",sans-serif;font-weight:400;
  font-size:20px;color:var(--navy)}
.card p{margin-top:6px;text-align:center;font-size:10px;line-height:16px}
.cta{left:49px;top:745px;width:655px;height:91px}
.cta-text{left:66px;top:780px;font-family:"Roboto Condensed",sans-serif;font-size:19px;color:var(--white)}
.cta-phone{left:222px;top:779px;font-family:"Roboto Condensed",sans-serif;font-weight:700;font-size:20px;color:var(--white)}
.cta-note{left:398px;top:759px;width:270px;font-size:10px;line-height:16px}
.cta-mail{left:398px;top:795px;font-size:14px;color:var(--navy);display:flex;align-items:center;gap:6px}
.news-title{top:872px}
.news-item{top:909px;width:147px}
.news-photo{width:147px;height:78px}
.news-item p{margin-top:6px;padding-left:2px;font-size:10px;line-height:16px;color:var(--navy)}
.news-item time{display:block;padding-left:2px;font-size:9px;color:var(--body-text);margin-top:1px}
.footer{left:0;top:1076px;width:753px;height:124px;background:var(--navy)}
.footer-nav{left:50px;top:1094px;display:flex;gap:22px;font-size:13.5px;color:var(--white)}
.social{top:1088px;width:32px;height:32px;border-radius:50%}
.rule{left:49px;top:1136px;width:656px;height:1px;background:var(--rule)}
.f-icon{top:1149px;width:29px;height:29px;border-radius:50%;background:var(--white);display:flex;align-items:center;justify-content:center}
.f-text{font-size:9.5px;line-height:14px;color:var(--white)}
</style>
</head>
<body>

<div class="abs hero" role="img" aria-label="City skyline photo with tall towers under a bright sunlit sky"></div>
<div class="abs hero-glow"></div>
<div class="abs brand-mark"></div>
<div class="abs brand-name">HARROWGATE CAPITAL</div>

<nav class="abs nav">
  <a class="current" href="#">HOME</a>
  <a href="#" style="left:147px">ABOUT</a>
  <a href="#" style="left:226px">SERVICES</a>
  <a href="#" style="left:320px">RECENT TRANSACTIONS</a>
  <a href="#" style="left:493px">NEWS</a>
  <a href="#" style="left:568px">CONTACT</a>
</nav>

<h1 class="abs welcome-title">WELCOME TO <strong>HARROWGATE CAPITAL</strong></h1>
<p class="abs welcome-text">Lorem Ipsum is simply dummy text of the printing and typesetting industry. Lorem Ipsum has been the industry's standard dummy text ever since the 1500s, when an unknown printer took a galley of type and scrambled it to make a type specimen book.</p>

<div class="abs card" style="left:49px">
  <div class="card-photo" role="img" aria-label="Mortgage application form with glasses and pen" style="background:linear-gradient(135deg,#e9e7e2,#bdbab3)"></div>
  <h2>Loan Programs</h2>
  <p>Lorem Ipsum is simply dummy text of the printing and typesetting industry. Lorem Ipsum has been the industry.</p>
</div>
<div class="abs card" style="left:278px">
  <div class="card-photo" role="img" aria-label="Hands reviewing financial charts on paper" style="background:linear-gradient(135deg,#c9d4df,#f1f3f5 55%,#5d95c8)"></div>
  <h2>Lending Parameters</h2>
  <p>Lorem Ipsum is simply dummy text of the printing and typesetting industry. Lorem Ipsum has been the industry.</p>
</div>
<div class="abs card" style="left:508px">
  <div class="card-photo" role="img" aria-label="Business team meeting in an office" style="background:linear-gradient(135deg,#e5e7ea,#9aa3ad 60%,#2e3440)"></div>
  <h2>Investment Strategy</h2>
  <p>Lorem Ipsum is simply dummy text of the printing and typesetting industry. Lorem Ipsum has been the industry.</p>
</div>

<svg class="abs cta" viewBox="0 0 655 91" aria-hidden="true">
  <rect x="0.5" y="0.5" width="654" height="90" fill="var(--panel)" stroke="#cfd1d5"/>
  <polygon points="0,0 308,0 327,45.5 308,91 0,91" fill="var(--navy)"/>
  <circle cx="143" cy="46" r="19" fill="none" stroke="#fff" stroke-width="1.5"/>
  <path d="M136 37c2-1 3 0 4 3l1 2c0 1-1 2-2 3 1 3 3 5 6 6 1-1 2-2 3-2l2 1c3 1 4 2 3 4-1 2-3 3-5 3-7-1-13-7-14-14 0-3 0-5 2-6z" fill="#fff"/>
</svg>
<div class="abs cta-text">CALL US ON</div>
<div class="abs cta-phone">123 456 7890</div>
<p class="abs cta-note">Lorem Ipsum is simply dummy text of the printing and typesetting industry. Lorem Ipsum has been the industry.</p>
<div class="abs cta-mail">
  <svg width="16" height="12" viewBox="0 0 16 12" aria-hidden="true"><rect x="1" y="1" width="14" height="10" fill="none" stroke="var(--navy)" stroke-width="1.4"/><path d="M1 1l7 6 7-6" fill="none" stroke="var(--navy)" stroke-width="1.4"/></svg>
  info@harrowgatecapital.com
</div>

<h2 class="abs news-title">LATEST <strong>NEWS</strong></h2>

<article class="abs news-item" style="left:49px">
  <div class="news-photo" role="img" aria-label="Glass office tower against blue sky" style="background:linear-gradient(135deg,#1e3f8a,#3d7fd0 60%,#d7a56a)"></div>
  <p>Lorem Ipsum is simply dummy text of the printing.</p><time>07 January 2016</time>
</article>
<article class="abs news-item" style="left:218px">
  <div class="news-photo" role="img" aria-label="White office building with palm trees" style="background:linear-gradient(180deg,#8fb7e3,#e8ecef 50%,#7c8a6a)"></div>
  <p>Lorem Ipsum is simply dummy text of the printing.</p><time>07 January 2016</time>
</article>
<article class="abs news-item" style="left:388px">
  <div class="news-photo" role="img" aria-label="Colleagues working together at a desk" style="background:linear-gradient(135deg,#d9dde2,#8d96a0 60%,#2f3540)"></div>
  <p>Lorem Ipsum is simply dummy text of the printing.</p><time>07 January 2016</time>
</article>
<article class="abs news-item" style="left:558px">
  <div class="news-photo" role="img" aria-label="Sunlit city skyline" style="background:linear-gradient(180deg,#c3d1e0,#8b9097 55%,#5b5b5c)"></div>
  <p>Lorem Ipsum is simply dummy text of the printing.</p><time>07 January 2016</time>
</article>

<footer class="abs footer"></footer>
<nav class="abs footer-nav"><span>Home</span><span>About</span><span>Services</span><span>Recent Transactions</span><span>News</span><span>Contact</span></nav>
<div class="abs social" style="left:583px;background:var(--white)"></div>
<div class="abs social" style="left:632px;border:1.5px solid var(--white)"></div>
<div class="abs social" style="left:681px;border:1.5px solid var(--white)"></div>
<div class="abs rule"></div>

<div class="abs f-icon" style="left:48px"><svg width="10" height="14" viewBox="0 0 10 14"><path d="M5 0a5 5 0 0 1 5 5c0 4-5 9-5 9S0 9 0 5a5 5 0 0 1 5-5z" fill="var(--navy)"/><circle cx="5" cy="5" r="1.8" fill="#fff"/></svg></div>
<p class="abs f-text" style="left:80px;top:1149px;width:130px">Lorem Ipsum is simply dummy text of the printing.</p>
<div class="abs f-icon" style="left:218px"><svg width="13" height="13" viewBox="0 0 13 13"><path d="M2 1c1.5-1 2.5 0 3 2l.5 1c0 1-.7 1.5-1.4 2 .8 1.8 2 3 3.8 3.8.5-.7 1-1.4 2-1.4l1 .5c2 .5 3 1.5 2 3-1 1.2-2.5 1.4-4 1C5 11.6 1.4 8 .4 5 0 3.5.3 2 2 1z" fill="var(--navy)"/></svg></div>
<p class="abs f-text" style="left:255px;top:1156px">123 456 7890</p>
<div class="abs f-icon" style="left:388px"><svg width="13" height="10" viewBox="0 0 13 10"><rect x=".7" y=".7" width="11.6" height="8.6" fill="none" stroke="var(--navy)" stroke-width="1.3"/><path d="M.7.7l5.8 5 5.8-5" fill="none" stroke="var(--navy)" stroke-width="1.3"/></svg></div>
<p class="abs f-text" style="left:424px;top:1156px">info@harrowgatecapital.com</p>
<p class="abs f-text" style="left:558px;top:1149px;line-height:16px">© <strong>HARROWGATE CAPITAL</strong> - 2016.<br>All Rights Reserved.</p>

</body>
</html>
```